Sunny Hello Card

4x6 Referral card double sided

basic hand drawn outline attached
not meant to be interpreted exactly but use artistic license to create what you think is best

Logo images uploaded as well

The purpose of this card is to have existing clients refer others to our office and have both of them get rewarded, however we wont put in writing that the original person gets rewarded - rather we will tell them verbally

```html
<!DOCTYPE html>
<html lang="en">
<head>
<meta charset="utf-8">
<title>Sunny Hello Dental – Referral Card</title>
<link href="https://fonts.googleapis.com/css2?family=Josefin+Sans:wght@700&family=Poppins:wght@500;600;800&display=swap" rel="stylesheet">
<style>
  :root {
    --page: #d3d3d3;
    --blue: #1a9cc8;
    --blue-deep: #0f8fbf;
    --blue-light: #3bb4d6;
    --orange: #f4982a;
    --white: #ffffff;
    --ink: #222222;
    --brand: #1a86b3;
    --leaf: #4a9a4a;
    --mist: #e9f3f1;
  }
  * { margin: 0; padding: 0; box-sizing: border-box; }
  html, body {
    width: 859px; height: 1200px; overflow: hidden;
    background: var(--page);
    font-family: "Poppins", sans-serif;
  }
  .card {
    position: absolute; left: 62px;
    width: 735px; height: 489px;
    background: var(--white);
    overflow: hidden;
    box-shadow: 0 4px 8px rgba(0,0,0,.35);
  }
  .card--front { top: 65px; }
  .card--back { top: 635px; }

  .foliage-wash {
    position: absolute; inset: 0 0 auto 0; height: 320px;
    background:
      radial-gradient(ellipse at 8% 10%, rgba(74,154,74,.35), transparent 35%),
      radial-gradient(ellipse at 95% 10%, rgba(74,154,74,.35), transparent 30%),
      radial-gradient(ellipse at 30% 0%, rgba(244,190,80,.3), transparent 35%),
      linear-gradient(180deg, var(--mist), var(--white));
  }
  .family-photo {
    position: absolute; left: 255px; top: 0; width: 480px; height: 330px;
    background:
      radial-gradient(ellipse at 60% 55%, #c9b8a6 0%, #e6dfd6 45%, transparent 75%),
      linear-gradient(90deg, rgba(240,238,234,0) 0%, #efece8 25%, #ebe8e3 100%);
  }
  .brand { position: absolute; text-align: center; }
  .brand__dot {
    display: block; margin: 0 auto;
    border-radius: 50%; background: var(--leaf);
  }
  .brand__name {
    display: block; color: var(--brand);
    font-family: "Poppins", sans-serif; font-weight: 600;
    white-space: nowrap;
  }
  .card--front .brand { left: 40px; top: 62px; width: 216px; }
  .card--front .brand__dot { width: 80px; height: 80px; }
  .card--front .brand__name { font-size: 29px; margin-top: 22px; line-height: 1.1; }
  .card--back .brand { left: 267px; top: 27px; width: 200px; }
  .card--back .brand__dot { width: 56px; height: 56px; }
  .card--back .brand__name { font-size: 22px; margin-top: 14px; }

  .waves { position: absolute; left: 0; top: 0; width: 735px; height: 489px; }

  .headline { position: absolute; left: 0; top: 0; width: 735px; height: 489px; }
  .headline text {
    font-family: "Josefin Sans", sans-serif; font-weight: 700; fill: var(--white);
  }
  .reward-copy {
    position: absolute; left: 421px; top: 362px;
    color: var(--white); font-weight: 800; font-size: 24px; line-height: 30px;
    white-space: nowrap;
  }
  .reward-badge {
    position: absolute; left: 596px; top: 357px; width: 98px; height: 98px;
    border-radius: 50%; background: var(--white);
    display: flex; align-items: center; justify-content: center;
    color: var(--orange); font-family: "Josefin Sans", sans-serif; font-weight: 700;
  }
  .reward-badge__currency { font-size: 24px; margin-top: -8px; }
  .reward-badge__amount { font-size: 50px; letter-spacing: -1px; }

  .signature-field {
    position: absolute; top: 210px; width: 300px;
    border-top: 1px solid var(--ink); text-align: center;
    font-weight: 600; font-size: 16px; color: var(--ink); padding-top: 6px;
  }
  .signature-field--new { left: 43px; }
  .signature-field--referrer { left: 399px; padding-top: 3px; }

  .contact { position: absolute; left: 43px; color: var(--white); font-weight: 500; font-size: 20px; line-height: 24px; white-space: nowrap; }
  .contact--phone { top: 327px; }
  .contact--address { top: 366px; }
  .contact__icon {
    position: absolute; left: 0; top: 0; width: 22px; height: 22px;
    background: var(--white); border-radius: 50%;
    display: flex; align-items: center; justify-content: center;
  }
  .contact__text { margin-left: 34px; display: block; }
  .website {
    position: absolute; left: 338px; top: 389px; width: 368px; height: 26px;
    background: var(--white); border-radius: 4px;
    color: var(--ink); font-size: 17px; font-weight: 500;
    display: flex; align-items: center; justify-content: center;
  }
  .call-to-action {
    position: absolute; left: 0; top: 0; width: 735px; height: 489px;
  }
  .call-to-action text {
    font-family: "Josefin Sans", sans-serif; font-weight: 700; fill: var(--white);
  }
</style>
</head>
<body>

<section class="card card--front">
  <div class="foliage-wash" role="img" aria-label="Watercolour wash with tropical leaves and gold splashes"></div>
  <div class="family-photo" role="img" aria-label="Photo of a smiling family of four taking a selfie on a bed"></div>

  <div class="brand">
    <span class="brand__dot"></span>
    <span class="brand__name">Sunny Hello<br>Dental</span>
  </div>

  <svg class="waves" viewBox="0 0 735 489" aria-hidden="true">
    <defs>
      <linearGradient id="blueFront" x1="0" y1="0" x2="0" y2="1">
        <stop offset="0" stop-color="#0f8fbf"/>
        <stop offset="1" stop-color="#3bb4d6"/>
      </linearGradient>
    </defs>
    <path d="M0 292 C150 225 330 220 470 285 C590 335 680 290 735 240 L735 489 L0 489 Z" fill="#f4982a"/>
    <path d="M0 303 C150 250 310 250 440 300 C560 345 660 340 735 300 L735 489 L0 489 Z" fill="#ffffff"/>
    <path d="M0 307 C150 256 310 256 440 306 C560 350 660 346 735 306 L735 489 L0 489 Z" fill="url(#blueFront)"/>
  </svg>

  <svg class="headline" viewBox="0 0 735 489" aria-label="Spread the smile">
    <defs>
      <path id="arcSpread" d="M32 392 Q205 300 378 392"/>
    </defs>
    <text font-size="72"><textPath href="#arcSpread" textLength="345" lengthAdjust="spacingAndGlyphs">SPREAD</textPath></text>
    <text x="42" y="446" font-size="70" textLength="316" lengthAdjust="spacingAndGlyphs" transform="rotate(2 200 420)">THE SMILE</text>
  </svg>

  <p class="reward-copy">Your Friend<br>or Family<br>Recieves</p>
  <div class="reward-badge"><span class="reward-badge__currency">$</span><span class="reward-badge__amount">25</span></div>
</section>

<section class="card card--back">
  <div class="foliage-wash" role="img" aria-label="Watercolour wash with tropical leaves and gold splashes"></div>

  <div class="brand">
    <span class="brand__dot"></span>
    <span class="brand__name">Sunny Hello Dental</span>
  </div>

  <div class="signature-field signature-field--new">New Patient’s Name</div>
  <div class="signature-field signature-field--referrer">Your’s Name</div>

  <svg class="waves" viewBox="0 0 735 489" aria-hidden="true">
    <defs>
      <linearGradient id="blueBack" x1="0" y1="0" x2="0" y2="1">
        <stop offset="0" stop-color="#0f8fbf"/>
        <stop offset="1" stop-color="#3bb4d6"/>
      </linearGradient>
    </defs>
    <path d="M0 320 C120 270 260 260 400 300 C540 345 650 330 735 258 L735 489 L0 489 Z" fill="#f4982a"/>
    <path d="M0 330 C130 282 260 282 400 330 C520 372 650 375 735 320 L735 489 L0 489 Z" fill="#ffffff"/>
    <path d="M0 334 C130 287 260 287 400 335 C520 377 650 380 735 326 L735 489 L0 489 Z" fill="url(#blueBack)"/>
  </svg>

  <div class="contact contact--phone">
    <span class="contact__icon">
      <svg width="13" height="13" viewBox="0 0 24 24"><path d="M6.6 10.8a15 15 0 0 0 6.6 6.6l2.2-2.2a1 1 0 0 1 1-.25 11.4 11.4 0 0 0 3.6.57 1 1 0 0 1 1 1V20a1 1 0 0 1-1 1A17 17 0 0 1 3 4a1 1 0 0 1 1-1h3.5a1 1 0 0 1 1 1c0 1.25.2 2.45.57 3.57a1 1 0 0 1-.25 1z" fill="#222"/></svg>
    </span>
    <span class="contact__text">555-014-2380</span>
  </div>
  <div class="contact contact--address">
    <span class="contact__icon">
      <svg width="12" height="14" viewBox="0 0 24 28"><path d="M12 0a10 10 0 0 0-10 10c0 7.5 10 18 10 18s10-10.5 10-18A10 10 0 0 0 12 0zm0 14a4 4 0 1 1 0-8 4 4 0 0 1 0 8z" fill="#222"/></svg>
    </span>
    <span class="contact__text">1200 Palm Grove Lane<br>Brightwater, FL 33000</span>
  </div>

  <div class="website">www.sunnyhellodental.com</div>
  <svg class="call-to-action" viewBox="0 0 735 489" aria-label="Have them bring this card to their first visit">
    <text x="36" y="460" font-size="25" textLength="657" lengthAdjust="spacingAndGlyphs">HAVE THEM BRING THIS CARD TO THEIR FIRST VISIT</text>
  </svg>
</section>

</body>
</html>
```